Sales/Landing Page Redesign for Hunting product

I am looking for a redesign for https://trelwickgear.com/quarter-pad .

We want to add in the information for our new XL quarterpad found: https://trelwickgear.com/shop/hunting/xl-big-game-quarter-pad/

We also will be adding a spot for this video: https://www.vidnorla.com/watch?v=QzR8kLw3hTn

We like having the 3 options at the bottom, but the goal for this page is to sell the quarter pad.

Target Market(s)

Western Hunters, campers, outdoorsmen

Industry/Entity Type

Hunting

Number of Pages Required

1 page

Font styles to use
Sans Serif

Requirements
Must have
• a clean design that is geared to sell the product.

```html
<!DOCTYPE html>
<html lang="en">
<head>
<meta charset="utf-8">
<title>Trelwick Quarter Pads</title>
<link href="https://fonts.googleapis.com/css2?family=Montserrat:ital,wght@0,400;0,500;0,600;0,700;0,800;1,600&family=Open+Sans:wght@400;600&display=swap" rel="stylesheet">
<style>
:root{
  --red:#e8222b;
  --orange:#f0802a;
  --dark:#2d3137;
  --darker:#24282d;
  --ink:#1f2226;
  --muted:#6b7078;
  --light:#f6f7f9;
  --white:#ffffff;
}
*{margin:0;padding:0;box-sizing:border-box}
html,body{width:1200px;height:3556px;overflow:hidden}
body{font-family:"Open Sans",Arial,sans-serif;color:var(--ink);background:var(--white);position:relative}
h1,h2,h3,h4,.btn,.brand,.nav a{font-family:"Montserrat",Arial,sans-serif}
section,header,footer{position:absolute;left:0;width:1200px}
.btn{display:inline-block;background:var(--red);color:var(--white);font-size:11px;font-weight:700;letter-spacing:.06em;text-transform:uppercase;padding:12px 26px;border-radius:22px;text-decoration:none}

/* hero */
.hero{top:0;height:552px;background:radial-gradient(ellipse at 30% 60%,#4a3a34 0%,#1c1a1a 55%,#0c0c0d 100%)}
.hero-nav{position:absolute;top:28px;left:60px;right:60px;display:flex;align-items:center;justify-content:space-between;z-index:2}
.brand{color:var(--white);font-size:26px;font-weight:800;letter-spacing:.04em}
.nav{display:flex;align-items:center;gap:34px}
.nav a{color:var(--white);font-size:12px;font-weight:600;text-decoration:none;letter-spacing:.04em}
.hero-photo{position:absolute;left:0;top:0;width:560px;height:552px;background:linear-gradient(100deg,rgba(150,90,70,.35),rgba(30,25,25,0))}
.hero-copy{position:absolute;top:160px;left:170px;width:660px;text-align:center;color:var(--white);z-index:2}
.hero-copy h1{font-size:46px;line-height:1.12;font-weight:800}
.hero-copy p{margin-top:18px;font-size:14px;font-weight:600;letter-spacing:.06em}
.hero-copy .btn{margin-top:34px}
.hero-product{position:absolute;left:870px;top:160px;width:290px;height:360px;border-radius:14px 14px 40px 40px;background:linear-gradient(160deg,#f04a2c,#c61d1d 70%,#8c1414)}

/* guarantee band */
.guarantee{top:552px;height:136px;background:var(--dark);color:var(--white)}
.guarantee-copy{position:absolute;left:60px;top:26px;width:520px}
.guarantee-copy h3{color:var(--red);font-size:18px;font-weight:800}
.guarantee-copy p{margin-top:8px;font-size:11px;line-height:1.55;color:#d8dadd}
.subscribe{position:absolute;left:680px;top:52px;display:flex;gap:14px}
.subscribe .field{width:220px;height:36px;border:1px solid #6a6f76;border-radius:4px;color:#c8cbcf;font-size:12px;padding:10px 14px}
.subscribe .btn{padding:11px 22px}

/* problem */
.problem{top:688px;height:360px}
.problem-copy{position:absolute;left:130px;top:46px;width:420px}
.problem-copy h2{color:var(--red);font-size:24px;font-weight:800}
.problem-list{list-style:none;margin-top:18px}
.problem-list li{display:flex;align-items:center;gap:12px;font-size:14px;color:#3a3e44;margin-bottom:9px}
.better{margin-top:16px;font-family:"Montserrat",sans-serif;font-style:italic;font-weight:600;color:var(--orange);font-size:24px}
.problem-copy .btn{margin-top:20px}
.problem-photo{position:absolute;left:600px;top:0;width:600px;height:360px;background:linear-gradient(170deg,#b8c3cc 0%,#6d7a64 45%,#3f4a36 70%,#c0392b 100%)}

/* benefits */
.benefits{top:1048px;height:772px;background:var(--light);text-align:center}
.benefits h2{margin-top:190px;color:var(--red);font-size:22px;font-weight:800;letter-spacing:.02em}
.benefit-grid{position:absolute;left:300px;top:270px;width:600px;display:grid;grid-template-columns:repeat(3,1fr);row-gap:50px}
.benefit{display:flex;flex-direction:column;align-items:center}
.benefit svg{width:88px;height:88px}
.benefit p{margin-top:14px;font-size:13px;line-height:1.45;color:#3a3e44;width:170px}
.benefits .btn{position:absolute;left:508px;top:690px}

/* video */
.video{top:1820px;height:400px;background:var(--white)}
.laptop{position:absolute;left:360px;top:50px;width:480px}
.laptop-screen{height:290px;background:#111;border-radius:14px 14px 0 0;padding:14px}
.video-frame{position:relative;width:100%;height:100%;background:linear-gradient(135deg,#4a4238,#2a2622 60%,#3c3a36)}
.play{position:absolute;left:50%;top:50%;width:58px;height:58px;margin:-29px 0 0 -29px;border-radius:50%;background:#f2b233;display:flex;align-items:center;justify-content:center}
.laptop-base{height:14px;margin:0 -40px;background:linear-gradient(#d9dbde,#a9adb2);border-radius:0 0 14px 14px}

/* products */
.products{top:2220px;height:592px;background:var(--dark);text-align:center}
.products h2{margin-top:60px;color:var(--red);font-size:22px;font-weight:800}
.product-row{position:absolute;left:180px;top:150px;display:flex;gap:80px}
.product{width:220px;display:flex;flex-direction:column;align-items:center}
.product-card{width:220px;height:210px;background:var(--white);display:flex;align-items:center;justify-content:center}
.product-shot{width:150px;height:170px;border-radius:8px 8px 26px 26px}
.shot-red{background:linear-gradient(160deg,#f04a2c,#c0181c)}
.shot-orange{background:linear-gradient(160deg,#ff9a3a,#e2651a)}
.price{margin-top:22px;color:var(--red);font-family:"Montserrat",sans-serif;font-weight:700;font-size:14px}
.product .btn{margin-top:14px;padding:10px 22px}

/* reviews */
.reviews{top:2812px;height:488px;text-align:center}
.reviews h2{margin-top:72px;color:var(--red);font-size:22px;font-weight:800}
.review-row{position:absolute;left:100px;top:150px;display:flex;gap:40px;text-align:left}
.review{width:307px}
.review-head{display:flex;gap:16px;align-items:flex-start}
.avatar{width:64px;height:64px;border-radius:50%;flex:none}
.review-head h4{color:var(--red);font-size:14px;font-weight:600;line-height:1.3}
.stars{color:#f2b233;font-size:13px;letter-spacing:2px;margin-top:3px}
.reviewer{font-size:11px;color:var(--muted);font-weight:600;text-transform:uppercase;margin-top:2px}
.review p{margin-top:18px;font-size:12px;line-height:1.6;color:#8a8f96}
.dots{position:absolute;left:0;width:100%;top:420px;display:flex;justify-content:center;gap:10px}
.dots span{width:8px;height:8px;border-radius:50%;background:#f2b233}

/* footer */
.site-footer{top:3300px;height:256px;background:var(--dark);color:var(--white)}
.footer-cols{position:absolute;left:200px;top:46px;display:flex;gap:0}
.footer-col{width:210px}
.footer-col h4{font-size:15px;font-weight:700;letter-spacing:.03em}
.footer-col p{margin-top:8px;font-size:11px;line-height:1.55;color:#c7cacf}
.socials{display:flex;gap:10px;margin-top:10px}
.socials span{width:18px;height:18px;border-radius:50%;background:var(--red)}
.footer-links{position:absolute;top:196px;left:0;width:100%;display:flex;justify-content:center;gap:26px;font-size:9px;color:#c7cacf;text-transform:uppercase;letter-spacing:.04em}
.copyright{position:absolute;top:228px;width:100%;text-align:center;font-size:9px;color:#9a9ea4}
</style>
</head>
<body>

<header class="hero">
  <div class="hero-photo" role="img" aria-label="Hunter quartering game meat in the field"></div>
  <div class="hero-product" role="img" aria-label="Red Trelwick quarter pad in its stuff sack"></div>
  <div class="hero-nav">
    <div class="brand">TRELWICK</div>
    <nav class="nav">
      <a href="#">MEALS</a>
      <a href="#">QUARTER PADS</a>
      <a class="btn" href="#">Shop Now</a>
    </nav>
  </div>
  <div class="hero-copy">
    <h1>Quarter pads to keep<br>your meat clean</h1>
    <p>100% WATERPROOF • LIGHTWEIGHT • QUALITY GUARANTEE</p>
    <a class="btn" href="#">Buy Now</a>
  </div>
</header>

<section class="guarantee">
  <div class="guarantee-copy">
    <h3>100% QUALITY GUARANTEE</h3>
    <p>We've designed our Quarter Pads for maximum performance and durability so you can hunt, pack and camp with confidence. If anything isn't right with your pad, just reach out to our team and we'll make it right.</p>
  </div>
  <div class="subscribe">
    <div class="field">Your Email</div>
    <a class="btn" href="#">Subscribe</a>
  </div>
</section>

<section class="problem">
  <div class="problem-copy">
    <h2>DO YOU STILL...</h2>
    <ul class="problem-list">
      <li><svg width="18" height="10" viewBox="0 0 18 10"><path d="M0 5h15M11 1l4 4-4 4" fill="none" stroke="#3a3e44" stroke-width="1.5"/></svg>Lay your fresh meat on a rock?</li>
      <li><svg width="18" height="10" viewBox="0 0 18 10"><path d="M0 5h15M11 1l4 4-4 4" fill="none" stroke="#3a3e44" stroke-width="1.5"/></svg>Sew bed sheets together</li>
      <li><svg width="18" height="10" viewBox="0 0 18 10"><path d="M0 5h15M11 1l4 4-4 4" fill="none" stroke="#3a3e44" stroke-width="1.5"/></svg>Use a door tarp?</li>
      <li><svg width="18" height="10" viewBox="0 0 18 10"><path d="M0 5h15M11 1l4 4-4 4" fill="none" stroke="#3a3e44" stroke-width="1.5"/></svg>Lay your meat in a dirt?</li>
      <li><svg width="18" height="10" viewBox="0 0 18 10"><path d="M0 5h15M11 1l4 4-4 4" fill="none" stroke="#3a3e44" stroke-width="1.5"/></svg>Stuff the meat in old used pillow bags?</li>
    </ul>
    <div class="better">There is a better way.</div>
    <a class="btn" href="#">Select ur quarter pad</a>
  </div>
  <div class="problem-photo" role="img" aria-label="Quarter pad laid out on a mountainside with a pack"></div>
</section>

<section class="benefits">
  <h2>BE RESPONSIBLE. USE A QUARTER PAD</h2>
  <div class="benefit-grid">
    <div class="benefit"><svg viewBox="0 0 88 88"><circle cx="44" cy="44" r="40" fill="#fff" stroke="#e3e5e8" stroke-width="3"/><path d="M44 4a40 40 0 0 1 40 40" fill="none" stroke="#e8222b" stroke-width="3"/><path d="M30 45l8 8 18-18" fill="none" stroke="#2d3137" stroke-width="3"/></svg><p>Keep your meat<br>off the dirt</p></div>
    <div class="benefit"><svg viewBox="0 0 88 88"><circle cx="44" cy="44" r="40" fill="#fff" stroke="#e3e5e8" stroke-width="3"/><path d="M44 4a40 40 0 0 1 40 40" fill="none" stroke="#e8222b" stroke-width="3"/><path d="M30 45l8 8 18-18" fill="none" stroke="#2d3137" stroke-width="3"/></svg><p>Reusable</p></div>
    <div class="benefit"><svg viewBox="0 0 88 88"><circle cx="44" cy="44" r="40" fill="#fff" stroke="#e3e5e8" stroke-width="3"/><path d="M44 4a40 40 0 0 1 40 40" fill="none" stroke="#e8222b" stroke-width="3"/><path d="M30 45l8 8 18-18" fill="none" stroke="#2d3137" stroke-width="3"/></svg><p>Respect the animal by keeping it contamination free</p></div>
    <div class="benefit"><svg viewBox="0 0 88 88"><circle cx="44" cy="44" r="40" fill="#fff" stroke="#e3e5e8" stroke-width="3"/><path d="M44 4a40 40 0 0 1 40 40" fill="none" stroke="#e8222b" stroke-width="3"/><path d="M30 45l8 8 18-18" fill="none" stroke="#2d3137" stroke-width="3"/></svg><p>55 * 60 when open</p></div>
    <div class="benefit"><svg viewBox="0 0 88 88"><circle cx="44" cy="44" r="40" fill="#fff" stroke="#e3e5e8" stroke-width="3"/><path d="M44 4a40 40 0 0 1 40 40" fill="none" stroke="#e8222b" stroke-width="3"/><path d="M30 45l8 8 18-18" fill="none" stroke="#2d3137" stroke-width="3"/></svg><p>100% Waterproof</p></div>
    <div class="benefit"><svg viewBox="0 0 88 88"><circle cx="44" cy="44" r="40" fill="#fff" stroke="#e3e5e8" stroke-width="3"/><path d="M44 4a40 40 0 0 1 40 40" fill="none" stroke="#e8222b" stroke-width="3"/><path d="M30 45l8 8 18-18" fill="none" stroke="#2d3137" stroke-width="3"/></svg><p>Lightweight</p></div>
  </div>
  <a class="btn" href="#">Select ur quarter pad</a>
</section>

<section class="video">
  <div class="laptop">
    <div class="laptop-screen">
      <div class="video-frame" role="img" aria-label="Product video about the quarter pad">
        <div class="play"><svg width="20" height="22" viewBox="0 0 20 22"><path d="M2 1l17 10L2 21z" fill="#fff"/></svg></div>
      </div>
    </div>
    <div class="laptop-base"></div>
  </div>
</section>

<section class="products">
  <h2>CHOOSE YOUR QUARTER PAD</h2>
  <div class="product-row">
    <div class="product"><div class="product-card"><div class="product-shot shot-red" role="img" aria-label="Red quarter pad in stuff sack"></div></div><div class="price">$19.95</div><a class="btn" href="#">Buy Now</a></div>
    <div class="product"><div class="product-card"><div class="product-shot shot-orange" role="img" aria-label="Orange quarter pad in stuff sack"></div></div><div class="price">$24.95</div><a class="btn" href="#">Buy Now</a></div>
    <div class="product"><div class="product-card"><div class="product-shot shot-red" role="img" aria-label="XL big game quarter pad in stuff sack"></div></div><div class="price">$29.95</div><a class="btn" href="#">Buy Now</a></div>
  </div>
</section>

<section class="reviews">
  <h2>WHAT OTHERS ARE SAYING?</h2>
  <div class="review-row">
    <div class="review">
      <div class="review-head"><div class="avatar" style="background:#8a6a52" role="img" aria-label="Customer portrait"></div><div><h4>Best product ever<br>hands downs</h4><div class="stars">★★★★★</div><div class="reviewer">Rowan Hale</div></div></div>
      <p>Packed it on a ten day elk hunt and it kept every quarter clean and cool. Rinses off fast, folds small and weighs next to nothing in my pack. I won't head into the backcountry without one again.</p>
    </div>
    <div class="review">
      <div class="review-head"><div class="avatar" style="background:#9a7a60" role="img" aria-label="Customer portrait"></div><div><h4>Best product ever<br>hands downs</h4><div class="stars">★★★★★</div><div class="reviewer">Ellis Marsh</div></div></div>
      <p>No more dirt, needles or bugs on the meat. The pad is big enough for a full hindquarter and still dries quickly in camp. Simple gear that does exactly what it promises every single time out.</p>
    </div>
    <div class="review">
      <div class="review-head"><div class="avatar" style="background:#b08a6a" role="img" aria-label="Customer portrait"></div><div><h4>Best product ever<br>hands downs</h4><div class="stars">★★★★★</div><div class="reviewer">Nora Quill</div></div></div>
      <p>We used two pads on a mule deer and the whole job felt cleaner and faster. Tough material, no tears after a season of use. Great value and a company that really stands behind its gear.</p>
    </div>
  </div>
  <div class="dots"><span></span><span></span><span></span></div>
</section>

<footer class="site-footer">
  <div class="footer-cols">
    <div class="footer-col" style="width:300px"><h4>FIND US</h4><p>412 Ridgeline Rd,<br>Fort Alder, MT 59002</p></div>
    <div class="footer-col" style="width:250px"><h4>EMAIL US</h4><p>hello@trelwickgear.com</p></div>
    <div class="footer-col" style="width:150px"><h4>CALL US</h4><p>(406) 555-0148</p></div>
    <div class="footer-col"><h4>SOCIAL LINKS</h4><div class="socials"><span></span><span></span><span></span></div></div>
  </div>
  <div class="footer-links"><span>My Account</span><span>FAQs</span><span>Terms of Service</span><span>Warranty</span><span>Return and Refund Policy</span><span>Privacy Policy</span><span>Guarantee</span></div>
  <div class="copyright">© 2024 Trelwick</div>
</footer>

</body>
</html>
```